Re-branding for Structural Engineering firm

We need new business cards as part of our current re-branding. We have a new logo (attached), so the card design should incorporate this color scheme. We are a structural engineering firm providing structural building design and seismic consulting services. The final design should communicate professionalism and stability, with a modern look and feel.

```html
<!DOCTYPE html>
<html lang="en">
<head>
<meta charset="utf-8">
<title>RVL Structural Engineering – Business Cards</title>
<link rel="stylesheet" href="https://fonts.googleapis.com/css2?family=Open+Sans:wght@400;600;700&display=swap">
<style>
  :root {
    --brand-blue: #1f75c0;
    --ink: #2b2b2b;
    --paper: #ffffff;
    --backdrop: #ecebe8;
  }
  * { margin: 0; padding: 0; box-sizing: border-box; }
  html, body { width: 1200px; height: 900px; overflow: hidden; }
  body {
    background: var(--backdrop);
    font-family: "Open Sans", Arial, sans-serif;
    position: relative;
  }
  .card {
    position: absolute;
    width: 530px;
    height: 303px;
    box-shadow: 0 4px 14px rgba(0,0,0,0.12);
    overflow: hidden;
  }
  /* Front */
  .card-front {
    left: 50px; top: 170px;
    background: var(--brand-blue);
    display: flex; align-items: center; justify-content: center;
  }
  .front-name {
    display: flex; align-items: center; gap: 14px;
    color: var(--paper);
    font-weight: 600; font-size: 28px; letter-spacing: 0.5px;
  }
  .front-square { width: 36px; height: 36px; background: var(--paper); flex: none; }

  /* Back */
  .card-back {
    left: 620px; top: 427px;
    background: var(--paper);
  }
  .back-name {
    position: absolute; left: 36px; top: 48px;
    color: var(--brand-blue);
    font-weight: 700; font-size: 24px; line-height: 30px; letter-spacing: 0.3px;
  }
  .person { position: absolute; left: 36px; top: 138px; }
  .person-name { color: var(--brand-blue); font-weight: 700; font-size: 15px; letter-spacing: 0.5px; }
  .person-title { color: var(--ink); font-size: 13px; margin-left: 8px; }
  .contacts { position: absolute; left: 44px; top: 196px; list-style: none; }
  .contacts li { display: flex; align-items: center; gap: 8px; font-size: 14px; color: var(--ink); line-height: 20px; }
  .contacts svg { width: 12px; height: 12px; fill: var(--brand-blue); flex: none; }
  .office { position: absolute; right: 26px; top: 168px; text-align: right; font-size: 11px; line-height: 15px; color: var(--ink); }
  .office-name { color: var(--brand-blue); }
</style>
</head>
<body>
  <section class="card card-front" aria-label="Business card front">
    <div class="front-name">
      <span class="front-square"></span>
      <span>RVL Structural Engineering</span>
    </div>
  </section>

  <section class="card card-back" aria-label="Business card back">
    <div class="back-name">RVL Structural Engineering</div>
    <div class="person">
      <div class="person-name">CAL DORNER, S.E.</div>
      <div class="person-title">Principal</div>
    </div>
    <ul class="contacts">
      <li><svg viewBox="0 0 12 12"><path d="M1 4c0-2 2-3 5-3s5 1 5 3l-2 1-1-1H4L3 5zM2 6h8v5H2z"/></svg>555.014.2291</li>
      <li><svg viewBox="0 0 12 12"><path d="M3 0h6v12H3zM4 1.5v8h4v-8z"/></svg>555.017.3408</li>
      <li><svg viewBox="0 0 12 12"><path d="M0 2h12v8H0zM1 3l5 4 5-4v-.2H1z"/></svg>cal@rvlse.com</li>
      <li><svg viewBox="0 0 12 12"><circle cx="6" cy="6" r="6"/></svg>www.rvlse.com</li>
    </ul>
    <div class="office">
      <div class="office-name">RVL Structural Engineering</div>
      <div>4170 Harbor Ridge Rd.,</div>
      <div>Ste 210 Lakeview, CA 90000</div>
    </div>
  </section>
</body>
</html>
```